Home page concept, possible logo colour change

There is no need to code a home page, we are just looking for concept ideas.
We have had a logo designed for a new company we are starting named Corvenhall Aluminium Windows & Doors. We are manufacturing bullet resistant window frames. We have had logo designed, we like the concept of the design, but the current colours (black and red) may not be the best option, especially when designing the website home page, and how it interacts with the logo colours. I have also attached the first draft of the home page which we are not happy with. The overall design/navigation is good, we have issues with the darkened out primary image and also the amount of red on the page, it just doesn't feel right. As mentioned before we are happy to look at colour changes to the logo.
Number of Pages Required
1 page
Look and feel
Each slider illustrates characteristics of the customer's brand and the style your logo design should communicate.

```html
<!DOCTYPE html>
<html lang="en">
<head>
<meta charset="utf-8">
<title>Corvenhall Aluminium Windows &amp; Doors</title>
<link href="https://fonts.googleapis.com/css2?family=League+Spartan:wght@400;500;600;700&family=Lexend:wght@500;600&family=Teko:wght@400;500&display=swap" rel="stylesheet">
<style>
:root{
  --navy:#0f2f52;
  --blue:#0a5aa0;
  --orange:#f7a400;
  --ink:#1a2a3a;
  --text:#4a5561;
  --grey:#ebebeb;
  --line:#d6d9dd;
  --white:#ffffff;
}
*{box-sizing:border-box;margin:0;padding:0}
html,body{width:1200px;height:3440px;overflow:hidden}
body{position:relative;background:var(--white);font-family:"League Spartan",Arial,sans-serif;color:var(--ink)}
.abs{position:absolute}
.brand{position:absolute;color:var(--navy);font-weight:700;line-height:1}
.brand .brand-name{display:block;font-size:27px;letter-spacing:-.5px}
.brand .brand-sub{display:block;font-size:7.5px;letter-spacing:.6px;text-transform:uppercase;margin-top:3px}
.nav{position:absolute;top:29px;left:396px;font-size:12px;color:var(--ink)}
.nav a{position:absolute;white-space:nowrap;text-decoration:none;color:inherit}
.nav a.active{color:var(--blue)}
.nav .phone{font-weight:600}
.enquiry-tab{position:absolute;left:968px;top:0;width:126px;height:96px;background:var(--blue);clip-path:polygon(0 0,100% 0,100% 88%,50% 100%,0 88%)}
.enquiry-tab span{position:absolute;top:30px;width:100%;text-align:center;color:#fff;font-weight:600;font-size:12.5px}
.hero{position:absolute;left:0;top:75px;width:1200px;height:459px;clip-path:polygon(0 0,100% 0,100% 71%,50% 100%,0 71%);
  background:linear-gradient(100deg,#d9dadb 0%,#ececec 40%,#e2e2e2 62%,#c9c9c9 100%)}
.hero-door{position:absolute;left:722px;top:112px;width:186px;height:340px;background:linear-gradient(180deg,#f4f4f4,#dcdcdc);border-radius:2px}
.hero-door::after{content:"";position:absolute;left:6%;right:6%;top:4%;bottom:6%;background:linear-gradient(90deg,#5a3b27,#7a5238,#563723)}
.eyebrow{position:absolute;color:var(--orange);font-size:14px;font-weight:500}
.heading{position:absolute;font-family:"Teko",sans-serif;font-weight:400;color:var(--navy);font-size:38px;line-height:1}
.copy{position:absolute;font-size:11px;line-height:18.5px;color:var(--text)}
.btn{position:absolute;display:flex;align-items:center;justify-content:center;gap:14px;color:#fff;font-weight:600;font-size:12px;height:30px}
.btn.orange{background:var(--orange)}
.btn.blue{background:var(--blue)}
.btn i{font-style:normal;font-size:11px}
.photo{position:absolute}
.feature{position:absolute;width:240px;text-align:center}
.feature h3{font-size:14.5px;font-weight:500}
.feature p{font-size:11px;line-height:14.5px;color:var(--text);margin-top:14px}
.feature-icon{position:absolute}
.hex{clip-path:polygon(0 18%,50% 0,100% 18%,100% 82%,50% 100%,0 82%)}
.acc-row{position:absolute;left:338px;width:524px;border-bottom:1px solid var(--line);font-size:13px;font-weight:500}
.acc-row .dot{position:absolute;right:20px;width:12px;height:12px;border-radius:50%;background:var(--blue);color:#fff;font-size:10px;line-height:12px;text-align:center}
.acc-row .dot.open{background:var(--orange)}
.field{position:absolute;border:1px solid #8a9bb0;color:#dbe3ec;font-size:9.5px;padding:9px 16px}
.footer-h{position:absolute;font-size:14px;font-weight:500;color:var(--ink)}
.footer-list{position:absolute;font-size:10.5px;color:var(--text);line-height:22.7px;list-style:none}
.social{position:absolute;width:30px;height:30px;border-radius:50%;background:var(--blue)}
.social.alt{background:var(--orange)}
.cert-placeholder{position:absolute;left:872px;top:3198px;width:66px;height:66px;border-radius:6px;background:#d9dde2}
</style>
</head>
<body>

<!-- header -->
<div class="brand" style="left:107px;top:22px">
  <span class="brand-name">Corvenhall</span>
  <span class="brand-sub">Aluminium Windows &amp; Doors</span>
</div>
<nav class="nav">
  <a class="active" style="left:0">Home</a>
  <a style="left:58px">About Us</a>
  <a style="left:134px">Our Products</a>
  <a style="left:231px">Why Corvenhall</a>
  <a style="left:358px">Contact Us</a>
  <a class="phone" style="left:440px"><svg width="10" height="10" viewBox="0 0 24 24" style="vertical-align:-1px;margin-right:6px"><path fill="#f7a400" d="M6.6 10.8a15 15 0 0 0 6.6 6.6l2.2-2.2c.3-.3.7-.4 1-.2 1.1.4 2.3.6 3.6.6.6 0 1 .4 1 1V20c0 .6-.4 1-1 1A17 17 0 0 1 3 4c0-.6.4-1 1-1h3.5c.6 0 1 .4 1 1 0 1.3.2 2.5.6 3.6.1.3 0 .7-.2 1z"/></svg>+61 2 7014 5528</a>
</nav>
<div class="enquiry-tab"><span>Make an Enquiry</span></div>

<!-- hero -->
<div class="hero" role="img" aria-label="Bright modern entrance with a timber front door, wall lamps and potted plants"></div>
<div class="hero-door" role="img" aria-label="Timber entrance door"></div>
<svg class="abs" style="left:0;top:0" width="1200" height="560" viewBox="0 0 1200 560">
  <polygon fill="#0a5aa0" points="195,442 600,528 1005,442 1005,446 600,540 195,446"/>
</svg>
<div class="abs" style="left:200px;top:156px;font-family:'Lexend',sans-serif;font-weight:500;font-size:22px;color:var(--ink)">Corvenhall</div>
<div class="abs" style="left:198px;top:196px;font-family:'Lexend',sans-serif;font-weight:600;font-size:58px;letter-spacing:-1px;color:var(--navy);line-height:1">Bullet Resistant</div>
<div class="abs" style="left:200px;top:263px;font-family:'Lexend',sans-serif;font-weight:500;font-size:36px;color:var(--navy);line-height:1">Window &amp; Doors</div>
<div class="btn orange" style="left:200px;top:328px;width:112px"><i>+</i>Contact Us<i>+</i></div>
<svg class="abs" style="left:1080px;top:238px" width="16" height="80" viewBox="0 0 16 80">
  <g fill="none" stroke="#555" stroke-width="1"><circle cx="8" cy="9" r="5"/><circle cx="8" cy="29" r="5"/><circle cx="8" cy="50" r="5"/><circle cx="8" cy="70" r="5"/></g>
  <circle cx="8" cy="29" r="2.5" fill="#555"/>
</svg>

<!-- about -->
<div class="eyebrow" style="left:200px;top:705px">About Us</div>
<div class="heading" style="left:200px;top:732px">Your First Line of Defence</div>
<p class="copy" style="left:200px;top:784px;width:375px">Lorem Ipsum is simply dummy text of the printing and typesetting industry. Lorem Ipsum has been the industry's standard dummy text ever since the 1500s, when an unknown printer.</p>
<p class="copy" style="left:200px;top:859px;width:385px">took a galley of type and scrambled it to make a type specimen book. It has survived not only five centuries, but also the leap into electronic ...</p>
<div class="abs" style="left:200px;top:923px;width:2px;height:32px;background:var(--blue)"></div>
<div class="abs" style="left:220px;top:932px;font-size:12px;font-weight:600;color:var(--blue)">More About Our Company →</div>
<div class="abs" style="left:732px;top:613px;width:268px;height:436px;border:1.5px solid var(--orange)"></div>
<div class="photo" style="left:744px;top:625px;width:244px;height:411px;background:linear-gradient(180deg,#cfc7c0,#bfb4aa 60%,#a9a6a4)" role="img" aria-label="Tiled entrance porch with a dark timber door and steps"></div>
<div class="photo" style="left:608px;top:788px;width:185px;height:252px;background:#fff"></div>
<div class="photo" style="left:613px;top:793px;width:175px;height:243px;background:linear-gradient(180deg,#dfe6ea,#7d8f86 45%,#3f72a8)" role="img" aria-label="Living room with floor-to-ceiling glass sliding doors"></div>

<!-- features -->
<svg class="feature-icon" style="left:290px;top:1128px" width="68" height="80" viewBox="0 0 68 80"><circle cx="34" cy="40" r="32" fill="none" stroke="#0a5aa0" stroke-width="2.5"/><path d="M20 41l9 9 19-19" fill="none" stroke="#f7a400" stroke-width="3"/></svg>
<svg class="feature-icon" style="left:566px;top:1128px" width="68" height="80" viewBox="0 0 68 80"><circle cx="34" cy="40" r="32" fill="none" stroke="#0a5aa0" stroke-width="2.5"/><rect x="22" y="24" width="24" height="32" fill="none" stroke="#1a2a3a" stroke-width="2"/><line x1="34" y1="24" x2="34" y2="56" stroke="#1a2a3a" stroke-width="2"/><rect x="26" y="30" width="4" height="10" fill="#f7a400"/></svg>
<svg class="feature-icon" style="left:840px;top:1128px" width="68" height="80" viewBox="0 0 68 80"><circle cx="34" cy="40" r="32" fill="none" stroke="#0a5aa0" stroke-width="2.5"/><rect x="20" y="36" width="18" height="16" fill="none" stroke="#1a2a3a" stroke-width="2"/><circle cx="42" cy="30" r="8" fill="none" stroke="#f7a400" stroke-width="2"/><path d="M38 30l3 3 5-5" fill="none" stroke="#1a2a3a" stroke-width="1.8"/></svg>
<div class="feature" style="left:204px;top:1237px"><h3>Premium Protection</h3><p>Lorem Ipsum is simply dummy text of the printing and typesetting industry. Lorem Ipsum has been the industry.</p></div>
<div class="feature" style="left:480px;top:1237px"><h3>Aesthetically Designed</h3><p>Lorem Ipsum is simply dummy text of the printing and typesetting industry. Lorem Ipsum has been the industry.</p></div>
<div class="feature" style="left:754px;top:1237px"><h3>Promptly Delivered</h3><p>Lorem Ipsum is simply dummy text of the printing and typesetting industry. Lorem Ipsum has been the industry.</p></div>
<div class="btn blue" style="left:545px;top:1347px;width:112px"><i>+</i>Contact Us<i>+</i></div>

<!-- products -->
<svg class="abs" style="left:0;top:1440px" width="1200" height="700" viewBox="0 0 1200 700">
  <path fill="#ebebeb" d="M0 124 L120 86 Q600 -30 1081 86 L1200 124 L1200 530 L600 673 L0 530 Z"/>
  <path fill="none" stroke="#0a5aa0" stroke-width="5" d="M120 86 Q600 -30 1081 86"/>
  <polygon fill="#0a5aa0" points="200,582 600,665 1000,582 1000,586 600,676 200,586"/>
</svg>
<div class="eyebrow" style="left:0;width:1200px;text-align:center;top:1543px">Our Products</div>
<div class="heading" style="left:0;width:1200px;text-align:center;top:1574px">Aluminium Windows &amp; Doors</div>
<div class="feature" style="left:204px;top:1660px"><h3 style="font-size:13.5px">Sliding Doors</h3><p>Lorem Ipsum is simply dummy text of the printing and typesetting industry. Lorem Ipsum has been the industry.</p></div>
<div class="feature" style="left:754px;top:1660px"><h3 style="font-size:13.5px">Folding Doors</h3><p>Lorem Ipsum is simply dummy text of the printing and typesetting industry. Lorem Ipsum has been the industry.</p></div>
<div class="feature" style="left:480px;top:1873px"><h3 style="font-size:13.5px">Casement Windows</h3><p>Lorem Ipsum is simply dummy text of the printing and typesetting industry. Lorem Ipsum has been the industry.</p></div>
<div class="photo hex" style="left:200px;top:1760px;width:250px;height:196px;background:linear-gradient(90deg,#d8d8d8,#3a4a3a 50%,#d0d0d0)" role="img" aria-label="Black framed aluminium sliding door opening to a garden"></div>
<div class="photo hex" style="left:475px;top:1651px;width:250px;height:198px;background:linear-gradient(90deg,#c8ab85,#eef1ee 30%,#9cbf8a 50%,#eef1ee 70%,#c8ab85)" role="img" aria-label="White casement windows framed by curtains"></div>
<div class="photo hex" style="left:750px;top:1760px;width:250px;height:196px;background:linear-gradient(90deg,#3c463e,#c9b59a 50%,#3c463e)" role="img" aria-label="Open folding doors leading to a timber deck"></div>
<div class="btn orange" style="left:531px;top:1997px;width:143px"><i>+</i>View All Products<i>+</i></div>

<!-- why -->
<div class="photo" style="left:0;top:2062px;width:244px;height:334px;background:linear-gradient(90deg,#1d2228,#dfe6ec 45%,#cfd8e0 80%,#1d2228);clip-path:polygon(0 5%,100% 0,100% 100%,0 88%)" role="img" aria-label="Open black aluminium casement window"></div>
<div class="photo" style="left:955px;top:2229px;width:245px;height:341px;background:linear-gradient(90deg,#e4e4e4,#f7f7f7 50%,#e8e8e8)" role="img" aria-label="White double French doors"></div>
<div class="eyebrow" style="left:0;width:1200px;text-align:center;top:2190px">Why Corvenhall</div>
<div class="heading" style="left:0;width:1200px;text-align:center;top:2222px">Superior Protection, Sleek Design</div>
<div class="abs" style="left:338px;top:2284px;width:524px;border-top:1px solid var(--line)"></div>
<div class="acc-row" style="top:2285px;height:38px;padding:11px 18px">Best Quality Products at Best Rates in the Market<span class="dot" style="top:13px">+</span></div>
<div class="acc-row" style="top:2323px;height:100px;padding:11px 18px">100% Australian products as Manufactured in Australia<span class="dot open" style="top:13px">–</span>
  <p style="font-size:10.5px;line-height:18.5px;color:var(--text);font-weight:400;margin-top:7px;width:420px">Lorem Ipsum is simply dummy text of the printing and typesetting industry. Lorem Ipsum has been the industry's standard dummy text ever since the 1500s, when an unknown printer.</p></div>
<div class="acc-row" style="top:2423px;height:37px;padding:11px 18px">Custom Designed as per Customers Requirements<span class="dot" style="top:13px">+</span></div>
<div class="acc-row" style="top:2460px;height:38px;padding:11px 18px">Best Support Services on all Purchased Products<span class="dot" style="top:13px">+</span></div>
<div class="btn blue" style="left:531px;top:2531px;width:138px"><i>+</i>Make an Enquiry<i>+</i></div>

<!-- footer background -->
<div class="abs" style="left:0;top:2950px;width:1200px;height:490px;background:linear-gradient(180deg,#eaeaea,#f4f4f4)"></div>

<!-- enquiry -->
<svg class="abs" style="left:0;top:2610px" width="1200" height="500" viewBox="0 0 1200 500">
  <path fill="#0f2f52" d="M0 113 L120 87 Q600 -40 1081 87 L1200 113 L1200 347 L600 487 L0 347 Z"/>
  <path fill="none" stroke="#0a5aa0" stroke-width="5" d="M120 87 Q600 -40 1081 87"/>
  <polygon fill="#0a5aa0" points="200,392 600,480 1000,392 1000,397 600,490 200,397"/>
</svg>
<div class="eyebrow" style="left:0;width:1200px;text-align:center;top:2715px">Make an Enquiry</div>
<div class="heading" style="left:0;width:1200px;text-align:center;top:2745px;color:#fff">Request A Free Estimate</div>
<div class="field" style="left:344px;top:2795px;width:249px;height:30px">Name</div>
<div class="field" style="left:606px;top:2795px;width:250px;height:30px">Phone</div>
<div class="field" style="left:344px;top:2839px;width:512px;height:30px">Email</div>
<div class="field" style="left:344px;top:2884px;width:512px;height:65px">Message ...</div>
<div class="btn orange" style="left:557px;top:2964px;width:87px"><i>+</i>Send<i>+</i></div>

<!-- footer -->
<div class="brand" style="left:200px;top:3182px">
  <span class="brand-name" style="font-size:34px">Corvenhall</span>
  <span class="brand-sub" style="font-size:8.5px">Aluminium Windows &amp; Doors</span>
</div>
<div class="abs" style="left:240px;top:3275px;width:140px;height:1px;background:var(--line)"></div>
<div class="social" style="left:245px;top:3260px"></div>
<div class="social alt" style="left:295px;top:3260px"></div>
<div class="social" style="left:344px;top:3260px"></div>

<div class="footer-h" style="left:474px;top:3162px">Contact us</div>
<div class="abs" style="left:474px;top:3198px;font-size:12px;color:var(--ink)"><span style="color:var(--orange);margin-right:12px">☎</span>+61 2 7014 5528</div>
<div class="abs" style="left:474px;top:3230px;font-size:10.5px;color:var(--text)"><span style="display:inline-block;width:9px;height:7px;background:var(--orange);margin-right:14px"></span>hello@corvenhall-example.com</div>
<svg class="abs" style="left:474px;top:3261px" width="9" height="12" viewBox="0 0 9 12"><path fill="#f7a400" d="M4.5 0A4.5 4.5 0 0 0 0 4.5C0 8 4.5 12 4.5 12S9 8 9 4.5A4.5 4.5 0 0 0 4.5 0zm0 6.3a1.8 1.8 0 1 1 0-3.6 1.8 1.8 0 0 1 0 3.6z"/></svg>
<div class="abs" style="left:497px;top:3260px;font-size:10.5px;line-height:18.5px;color:var(--text)">Sydney<br>48 Ferrier Lane Sydney,<br>NSW 2010 AU</div>

<div class="footer-h" style="left:704px;top:3162px">Quick links</div>
<ul class="footer-list" style="left:704px;top:3194px">
  <li>Home</li><li>About Us</li><li>Our Products</li><li>Why Corvenhall</li><li>Blog</li><li>Contact Us</li>
</ul>

<div class="footer-h" style="left:850px;top:3162px">Quality Assurance</div>
<div class="cert-placeholder" role="img" aria-label="Quality certification badge"></div>

<div class="abs" style="left:200px;top:3376px;font-size:10.5px;color:var(--text)">© 2023 <b style="color:var(--navy)">Corvenhall</b>. All Right Reserved</div>
<svg class="abs" style="left:1092px;top:3370px" width="16" height="18" viewBox="0 0 16 18"><polygon points="8,0 16,18 8,13 0,18" fill="#0a5aa0"/></svg>

</body>
</html>
```